Website 950x200 Header w/ logo

I'm in need of a website header for a new site called DaysofMarco.com

The site is basically a glorified blog for myself to write my thoughts about politics, sports, TV shows, current events, whatever. I have a lot of interests.

The site is going to look very very similar to http://www.quickmakerhub.example/4937261/6-tips-to-hold-the-lead-in-design-work

but instead of having a dynamic header that becomes the picture with each article, its just going to be a static header in which I'd like to have the name of the site (Days of Marco) and some kind of logo, pictures, etc - I'm totally open to anything. The only thing is it needs to have a dark (probably black) background and needs to be 950x200px.

I envision a black background, with gray and white as the primary colors and then some secondary colors potentially, but again I'm open to anything as long as it's on the black background or some kind of charcoal gray or wahtever. On the site the black part will go all the way from the left of the screen to the right no matter what the window size, but I'd like to keep all the content inside of 950x200px

email me marco.pellwin@mailnest.example if you have any questions. Thanks!

Industry/Entity Type

Tv

```html
<!DOCTYPE html>
<html lang="en">
<head>
<meta charset="utf-8">
<title>Days of Marco — Header</title>
<link href="https://fonts.googleapis.com/css2?family=Kaushan+Script&display=swap" rel="stylesheet">
<style>
  :root {
    --bg-black: #000000;
    --dot-light: #d8d8d8;
    --dot-mid: #6a6a6a;
    --title-top: #ffffff;
    --title-mid: #d6d6d6;
    --title-bottom: #7a7a7a;
  }
  html, body {
    margin: 0;
    padding: 0;
    overflow: hidden;
    background: var(--bg-black);
  }
  .site-header {
    position: relative;
    width: 1200px;
    height: 253px;
    background: var(--bg-black);
    overflow: hidden;
  }
  .halftone-band {
    position: absolute;
    left: 0;
    top: 0;
    width: 1200px;
    height: 125px;
    background: linear-gradient(
      to bottom,
      rgba(216, 216, 216, 0.55) 0%,
      rgba(140, 140, 140, 0.35) 35%,
      rgba(80, 80, 80, 0.15) 70%,
      rgba(0, 0, 0, 0) 100%
    );
  }
  .site-title {
    position: absolute;
    right: 38px;
    top: 92px;
    margin: 0;
    font-family: "Kaushan Script", cursive;
    font-weight: 400;
    font-size: 112px;
    line-height: 1;
    letter-spacing: 4px;
    white-space: nowrap;
    background: linear-gradient(
      to bottom,
      var(--title-top) 20%,
      var(--title-mid) 55%,
      var(--title-bottom) 95%
    );
    -webkit-background-clip: text;
    background-clip: text;
    color: transparent;
  }
</style>
</head>
<body>
  <header class="site-header">
    <div class="halftone-band" role="img" aria-label="Halftone dot pattern fading from light gray at the top into black"></div>
    <h1 class="site-title">Days of Marco</h1>
  </header>
</body>
</html>
```